A gateway to the eyes of potential Tenlar Candidates and Clients

We are looking for a brochure that will grab attention, all most along the lines of an infogram. The business supplies people to the construction sector. So we want it simple but sharp.

I would like the brochure to be able to have a half fold effect when printed but the main focus will be to use it in an e-brochure format.

Main pages will be as follows:

About Us: Which will have a bit about the management team and some pictures.

Services: information for both candidate and clients.

Why us?:

Contact: Location, contact numbers etc.

FOR CONTENTS:
website will give you the content required. www.tenlarconstruction.co.uk
Updates

Project Deadline Extended Reason: Project was moved from a flyer to a brochure and the logo didn't upload. So I will be uploading my new logo and it will give additional time to get designs in. Cheers Added Monday, June 20, 2016

Target Market(s)

Clients and candidates for the construction market

Industry/Entity Type

Business

Requirements
Must have
• Bold and strong images of the construction sector. A simple to read format. Also needs to look good in an electronic format.
Nice to have
• I like the idea of a black and white model but with certain parts of the images highlighted in our colours.
Should not have
• Too much of a complex lay out.

```html
<!DOCTYPE html>
<html lang="en">
<head>
<meta charset="utf-8">
<title>Tenlar Construction – Brochure Cover</title>
<link rel="stylesheet" href="https://fonts.googleapis.com/css2?family=Oswald:wght@300;400&family=Tinos:ital,wght@0,700;1,700&display=swap">
<style>
  :root {
    --blue-deep: #1f5fb4;
    --blue-mid: #1b8fd0;
    --blue-light: #22b5e3;
    --orange: #f5a21a;
    --orange-light: #fbc12d;
    --white: #ffffff;
    --page-grey: #f1f2f3;
    --backdrop: #e6e7e9;
    --ghost: #c9cbce;
  }
  html, body {
    margin: 0;
    padding: 0;
    width: 1200px;
    height: 802px;
    overflow: hidden;
    background: var(--backdrop);
  }
  .canvas {
    position: relative;
    width: 1200px;
    height: 802px;
    display: flex;
    justify-content: center;
    align-items: center;
  }
  .spread {
    display: flex;
    box-shadow: 0 6px 18px rgba(0,0,0,0.12);
  }
  .page {
    position: relative;
    width: 560px;
    height: 722px;
    overflow: hidden;
    background: var(--white);
  }
  .page svg { position: absolute; inset: 0; display: block; }

  /* back page */
  .back-cover .ghost-name {
    position: absolute;
    left: 0; right: 0;
    top: 292px;
    text-align: center;
    font-family: "Oswald", sans-serif;
    font-weight: 400;
    color: var(--ghost);
    line-height: 1;
  }
  .back-cover .ghost-name .word { font-size: 44px; letter-spacing: 4px; display: block; }
  .back-cover .ghost-name .sub { font-size: 11px; letter-spacing: 6px; display: block; margin-top: 4px; }

  .contact {
    position: absolute;
    left: 54px;
    top: 470px;
    color: var(--white);
    font-family: "Tinos", serif;
  }
  .contact .call-label { font-size: 20px; font-weight: 700; letter-spacing: 1px; margin: 0; }
  .contact .phone { font-size: 24px; font-style: italic; font-weight: 700; margin: 0 0 14px; letter-spacing: 1px; }
  .contact .address { display: flex; gap: 10px; font-size: 15px; font-style: italic; font-weight: 700; line-height: 1.15; margin: 0 0 24px; }
  .contact .address svg { position: static; flex: none; }
  .contact .web { font-size: 14px; font-weight: 700; margin: 0; }

  /* front page */
  .brand {
    position: absolute;
    left: 70px;
    top: 78px;
    display: flex;
    align-items: center;
    gap: 10px;
    font-family: "Oswald", sans-serif;
    font-weight: 400;
    color: var(--orange);
  }
  .brand .mark { width: 30px; height: 30px; background: var(--blue-mid); }
  .brand .name { font-size: 30px; letter-spacing: 2px; line-height: 1; }

  .tagline {
    position: absolute;
    right: 34px;
    top: 520px;
    text-align: right;
    color: var(--white);
    font-family: "Oswald", sans-serif;
    font-weight: 300;
    line-height: 1.02;
    margin: 0;
  }
  .tagline .lead { display: block; font-size: 40px; font-weight: 400; }
  .tagline .line { display: block; font-size: 27px; }
  .front-web {
    position: absolute;
    right: 40px;
    top: 666px;
    margin: 0;
    color: var(--white);
    font-family: "Tinos", serif;
    font-weight: 700;
    font-size: 14px;
  }
</style>
</head>
<body>
<main class="canvas">
  <div class="spread">

    <section class="page back-cover">
      <svg viewBox="0 0 560 722" width="560" height="722" aria-hidden="true">
        <defs>
          <linearGradient id="blueBandBack" x1="0" y1="0" x2="1" y2="1">
            <stop offset="0" stop-color="var(--blue-light)"/>
            <stop offset="1" stop-color="var(--blue-deep)"/>
          </linearGradient>
          <linearGradient id="skylineFade" x1="0" y1="0" x2="0" y2="1">
            <stop offset="0" stop-color="#ffffff" stop-opacity="0"/>
            <stop offset="0.5" stop-color="#b9bcc0" stop-opacity="0.55"/>
            <stop offset="1" stop-color="#8e9297" stop-opacity="0.8"/>
          </linearGradient>
        </defs>
        <rect class="page-fill" width="560" height="722" fill="var(--page-grey)"/>
        <rect class="skyline-photo" role="img" aria-label="Faded black and white city skyline with construction cranes" x="110" y="360" width="450" height="362" fill="url(#skylineFade)"/>
        <polygon class="top-band" points="0,0 330,0 0,118" fill="url(#blueBandBack)"/>
        <polygon class="top-stripe" points="0,118 330,0 372,0 0,136" fill="var(--orange)"/>
        <polygon class="bottom-stripe" points="0,248 470,722 448,722 0,270" fill="var(--orange)"/>
        <polygon class="bottom-band" points="0,270 448,722 0,722" fill="url(#blueBandBack)"/>
      </svg>
      <div class="ghost-name" aria-hidden="true">
        <span class="word">TENLAR</span>
        <span class="sub">CONSTRUCTION</span>
      </div>
      <div class="contact">
        <p class="call-label">CALL US:</p>
        <p class="phone">01632 960418</p>
        <p class="address">
          <svg width="20" height="18" viewBox="0 0 20 18" aria-hidden="true"><path d="M10 1 L1 9 H4 V17 H8.5 V12 H11.5 V17 H16 V9 H19 Z" fill="var(--white)"/></svg>
          <span>Birch Corner, Kestrel Hill Rd<br>East Sussex RH99 2XA</span>
        </p>
        <p class="web">www.tenlarconstruction.co.uk</p>
      </div>
    </section>

    <section class="page front-cover">
      <svg viewBox="0 0 560 722" width="560" height="722" aria-hidden="true">
        <defs>
          <linearGradient id="blueField" x1="0.5" y1="0" x2="0.4" y2="1">
            <stop offset="0" stop-color="var(--blue-light)"/>
            <stop offset="0.55" stop-color="var(--blue-mid)"/>
            <stop offset="1" stop-color="var(--blue-deep)"/>
          </linearGradient>
          <linearGradient id="orangeTone" x1="0" y1="0" x2="1" y2="1">
            <stop offset="0" stop-color="var(--orange-light)"/>
            <stop offset="1" stop-color="var(--orange)"/>
          </linearGradient>
          <linearGradient id="siteTone" x1="0" y1="0" x2="1" y2="1">
            <stop offset="0" stop-color="#6fa6dc"/>
            <stop offset="0.5" stop-color="#3e6f9e"/>
            <stop offset="1" stop-color="#c9b98a"/>
          </linearGradient>
        </defs>
        <rect class="page-fill" width="560" height="722" fill="var(--white)"/>
        <polygon class="blue-field" points="230,0 560,0 560,722 0,722 0,660 560,120" fill="url(#blueField)"/>
        <polygon class="blue-field-lower" points="0,560 560,200 560,722 0,722" fill="url(#blueField)"/>
        <polygon class="corner-accent" points="455,0 560,0 560,112" fill="url(#orangeTone)"/>
        <polygon class="base-accent" points="20,615 200,722 20,722" fill="url(#orangeTone)"/>
        <g class="accent-tiles" fill="url(#orangeTone)">
          <rect x="115" y="420" width="70" height="70" transform="rotate(40 150 455)"/>
          <rect x="185" y="385" width="95" height="95" transform="rotate(40 232 432)"/>
          <rect x="185" y="500" width="42" height="42" transform="rotate(40 206 521)"/>
        </g>
        <g class="feature-frame" transform="rotate(40 320 290)">
          <rect x="170" y="140" width="300" height="300" fill="url(#orangeTone)"/>
          <rect x="182" y="152" width="276" height="276" fill="var(--white)"/>
          <rect class="site-photo" role="img" aria-label="Construction workers in hard hats and hi-vis vests guiding a crane lift between buildings" x="188" y="158" width="264" height="264" fill="url(#siteTone)"/>
        </g>
      </svg>
      <div class="brand">
        <span class="mark" aria-hidden="true"></span>
        <span class="name">TENLAR</span>
      </div>
      <h1 class="tagline">
        <span class="lead">YOUR LIFE</span>
        <span class="line">does not get</span>
        <span class="line">better by chance</span>
        <span class="line">it gets better by change</span>
      </h1>
      <p class="front-web">www.tenlarconstruction.co.uk</p>
    </section>

  </div>
</main>
</body>
</html>
```